New Letterhead

Improve the attached letterhead to make it more alive and corporate class using the company colors in the two companies logos available on the two companies website.

Industry/Entity Type

Construction Company

Requirements
Must have
• colours of the two logod
Nice to have
• Be more alive and professional
Should not have
• Any other colours besides the ones in the logos

```html
<!DOCTYPE html>
<html lang="en">
<head>
<meta charset="utf-8">
<title>Kestrel Build – Letterhead</title>
<link href="https://fonts.googleapis.com/css2?family=Lato:wght@400;700;900&family=Open+Sans:wght@400;600&display=swap" rel="stylesheet">
<style>
  :root {
    --teal: #3a97a5;
    --charcoal: #2b3035;
    --maroon: #8a1c1c;
    --text: #575b5f;
    --ink: #1f2326;
    --backdrop: #e6e7e8;
    --paper: #ffffff;
  }
  * { margin: 0; padding: 0; box-sizing: border-box; }
  html, body { width: 1040px; height: 1200px; overflow: hidden; }
  body { background: var(--backdrop); position: relative; }

  .sheet {
    position: absolute; left: 66px; top: 15px;
    width: 789px; height: 1017px;
    transform: scale(1.15); transform-origin: top left;
    background: var(--paper);
    font-family: "Open Sans", Arial, sans-serif;
    color: var(--text);
    box-shadow: 0 2px 10px rgba(0,0,0,0.12);
  }
  .tagline-band {
    position: absolute; left: 0; top: 0; width: 100%; height: 38px;
    background: var(--teal); color: #fff;
    font-family: "Lato", Arial, sans-serif; font-weight: 700; font-size: 12.5px;
    display: flex; align-items: center; justify-content: center; letter-spacing: -0.1px;
  }
  .brand-primary {
    position: absolute; left: 75px; top: 56px;
    font-family: "Lato", Arial, sans-serif; font-weight: 900; font-size: 30px;
    color: var(--charcoal); display: flex; align-items: center; gap: 8px; letter-spacing: -0.5px;
  }
  .brand-primary .mark { width: 14px; height: 14px; background: var(--teal); }
  .brand-partner {
    position: absolute; right: 84px; top: 54px; text-align: right;
    font-family: "Lato", Arial, sans-serif; font-weight: 700; color: var(--maroon);
    font-size: 17px; line-height: 1.05; letter-spacing: -0.3px;
  }
  .brand-partner small { display: block; font-size: 9px; letter-spacing: 1px; font-weight: 700; }

  .letter { position: absolute; left: 74px; top: 165px; width: 638px; font-size: 12.5px; }
  .issue-date { margin-bottom: 14px; }
  .recipient { line-height: 15.5px; margin-bottom: 42px; }
  .salutation { margin-bottom: 22px; }
  .letter p.body-copy {
    line-height: 23px; text-align: justify; hyphens: auto; margin-bottom: 22px;
  }
  .closing { margin-top: 34px; }
  .signatory { margin-top: 46px; font-size: 15px; color: var(--ink); }
  .signatory-role { margin-top: 4px; }

  .footer {
    position: absolute; left: 0; top: 876px; width: 100%; height: 130px;
    font-family: "Lato", Arial, sans-serif; font-size: 12.5px; line-height: 15.3px; color: var(--ink);
  }
  .footer-col { position: absolute; top: 0; }
  .footer-col .contact { margin-top: 9px; }
  .col-primary { left: 76px; top: 2px; }
  .col-primary .company, .col-primary .accent { color: var(--teal); }
  .col-partner { left: 282px; }
  .col-partner .company, .col-partner .accent { color: var(--maroon); }
  .col-legal { left: 528px; top: 42px; }
  .col-legal .directors { margin-top: 13px; padding-left: 2px; }
  .col-legal .directors span { display: block; padding-left: 58px; }
  .divider { position: absolute; top: 0; width: 2px; height: 114px; background: var(--teal); }
  .divider-a { left: 266px; }
  .divider-b { left: 507px; }

  .base-band { position: absolute; left: 0; bottom: 0; width: 100%; height: 12px; background: var(--charcoal); }
</style>
</head>
<body>
  <article class="sheet">
    <header class="tagline-band">BUILDING STRONGER FOUNDATIONS FOR EVERY PROJECT WE DELIVER</header>

    <div class="brand-primary"><span>KESTREL BUILD</span><span class="mark"></span></div>
    <div class="brand-partner">MORVALE<small>GROUP</small></div>

    <section class="letter">
      <div class="issue-date">Issuing Date: May 5, 2018</div>
      <div class="recipient">Name Of Employee Mr. XYZABC<br>Address of Employee<br>Address Line 2 etc..</div>
      <div class="salutation">Dear Mr.XYZABC</div>
      <p class="body-copy">Lorem Ipsum has been the industry's standard dummy text ever since the 1500s, when an unknown printer took a galley of type and scrambled it to make a type specimen book. It has survived not only five centuries, but also the leap into electronic typesetting, remaining essentially unchanged. It was popularised in the 1960s with the release of Letraset sheets containing Lorem Ipsum passages, and more recently with desktop publishing software like Aldus PageMaker including versions of Lorem Ipsum.</p>
      <p class="body-copy">Lorem Ipsum is simply dummy text of the printing and typesetting industry. Lorem Ipsum has been the industry's standard dummy text ever since the 1500s, when an unknown printer took a galley of type and scrambled it to make a type specimen book.</p>
      <p class="body-copy">It has survived not only five centuries, but also the leap into electronic typesetting, remaining essentially unchanged. It was popularised in the 1960s with the release of Letraset sheets containing Lorem IpsumIpsum passages.</p>
      <div class="closing">Yours Sincerely</div>
      <div class="signatory">Daniel Foster</div>
      <div class="signatory-role">Managing Director</div>
    </section>

    <footer class="footer">
      <div class="footer-col col-primary">
        <div class="company">Kestrel VP JV (Pty) Limited</div>
        <div>12 Alder Road<br>Parkview, Johannesburg<br>PO Box 51720, Rosebank, 2016<br>South Africa</div>
        <div class="contact">T:&nbsp; +27 (0)11 555 0142<br>www.<span class="accent">kestrelbuild</span>.com</div>
      </div>
      <div class="divider divider-a"></div>
      <div class="footer-col col-partner">
        <div class="company">Kestrel VP JV (Pty) Limited</div>
        <div>27 Oak Lane, Cnr Wren Avenue<br>Birchwood North,<br>Johannesburg 2198<br>South Africa</div>
        <div class="contact"><span class="accent">T:</span> +27 (0)11 555 0187<br><span class="accent">www.morvalegroup.com</span></div>
      </div>
      <div class="divider divider-b"></div>
      <div class="footer-col col-legal">
        <div>Registration No. 2017/204815/07<br>Trading as Kestrel VP JV (Pty) Limited</div>
        <div class="directors">Directors: Peter Lawson<span>Adrian</span></div>
      </div>
    </footer>

    <div class="base-band"></div>
  </article>
</body>
</html>
```